Delivery Performance Dashboard for Web Portal

We need you to design a dashboard for our web portal. We deliver sand and stone to construction jobsites. The attached screenshot is from our current web portal dashboard . It shows how much material has been delivered from an order.

Dump trucks will deliver multiple loads during the day and the dispatcher uses the dashboard to monitor if they need to add more trucks or less trucks to fulfill the order. An example would be, I need to ship 1,000 tons of sand to a jobsite and I plan to use 10 trucks during the day and that it will take 10 hours of hauling to complete the job. After 5 hours of hauling (50% the day is over), I should have delivered 500 tons of sand (50% of the order). But maybe there is a lot of traffic, and I only have delivered 300 tons. The dashboard will show that I am behind schedule and I might need to add 2 more trucks to the job.

Industry/Entity Type

Construction

Font styles to use
Sans Serif

Requirements
Must have
• We need a progress bar showing how much material has been delivered, how much material was requested to be delivered total and how much material should have been delivered at the current time. The goal is to show the user if the deliveries are ahead or behind the expected pace and why.
Nice to have
• The icons for plant, driving and jobsite show if the actual times have exceeded or beaten the planned times. Maybe you have other ideas to show the user if the trucks are sitting longer on the jobsite, at the plant to get loaded or driving to and from the jobsite.

```html
<!DOCTYPE html>
<html lang="en">
<head>
<meta charset="utf-8">
<title>Delivery Performance Dashboard</title>
<link href="https://fonts.googleapis.com/css2?family=Roboto:wght@300;400;500&display=swap" rel="stylesheet">
<style>
:root{
  --blue:#5a9bf0;
  --blue-dark:#4a8be6;
  --bg:#f6f7fb;
  --white:#ffffff;
  --ink:#1f2430;
  --muted:#8a8f9c;
  --line:#e3e6ee;
  --green:#22b53a;
  --red:#e02424;
}
*{box-sizing:border-box;margin:0;padding:0}
html,body{width:1200px;height:517px;overflow:hidden}
body{font-family:'Roboto',sans-serif;background:var(--bg);color:var(--ink);position:relative}
.topbar{position:absolute;left:0;top:0;width:1200px;height:33px;background:var(--white)}
.menu{position:absolute;left:14px;top:15px;width:11px}
.menu span{display:block;height:1.3px;background:var(--blue);margin-bottom:1.6px}
.top-icon{position:absolute;top:14px}
.bell-dot{position:absolute;left:996px;top:11px;width:3px;height:3px;border-radius:50%;background:var(--blue)}
.user{position:absolute;left:1006px;top:15px;text-align:right;width:38px;white-space:nowrap}
.user .name{font-size:4.2px;font-weight:500}
.user .role{font-size:3px;color:var(--blue)}
.avatar{position:absolute;left:1048px;top:7px;width:25px;height:25px;border-radius:50%;background:linear-gradient(135deg,#b99a84,#6d5a4e)}
.sidebar{position:absolute;left:0;top:33px;width:37px;height:484px;background:var(--blue)}
.sidebar .active{position:absolute;right:0;top:28px;width:2px;height:32px;background:var(--white)}
.sidebar svg{position:absolute;left:14px}
.page-title{position:absolute;left:58px;top:59px;font-size:16px;color:var(--blue);font-weight:400}
.search{position:absolute;left:204px;top:56px;width:176px;height:22px;background:var(--white);font-size:8px;color:#555;padding:6px 10px}
.search-btn{position:absolute;left:380px;top:56px;width:55px;height:22px;background:var(--blue)}
.search-btn svg{position:absolute;left:22px;top:6px}
.select{position:absolute;top:56px;height:22px;background:var(--white);font-size:8px;color:#555;padding:6px 13px}
.select:after{content:"";position:absolute;right:13px;top:9px;border:3.5px solid transparent;border-top:4px solid var(--blue-dark)}
.section{position:absolute;left:58px;top:101px;font-size:10.5px;color:var(--blue);font-weight:300}
.thead{position:absolute;left:0;top:128px;width:1010px;font-size:8.3px}
.row{position:absolute;left:0;width:1010px;height:36px;font-size:8.3px}
.row:after{content:"";position:absolute;left:58px;right:0;bottom:0;height:1px;background:var(--line)}
.c{position:absolute;top:50%;transform:translateY(-50%);white-space:nowrap}
.thead .c{top:4px;transform:none;color:var(--ink)}
.chk{left:58px;width:11px;height:11px;background:var(--white);border:1px solid #e8e9ee;border-radius:2px}
.id{left:83px}.org{left:163px}.dst{left:283px}.cus{left:422px}.sts{left:606px}
.tons{left:689px;width:112px;height:14px}
.tons .a{position:absolute;left:0;top:0;font-size:4px;color:var(--muted)}
.tons .b{position:absolute;right:0;top:0;font-size:4px;color:var(--blue)}
.tons .track{position:absolute;left:0;top:8px;width:112px;height:3px;border-radius:2px;background:#e7ecf5}
.tons .fill{position:absolute;left:0;top:0;height:3px;border-radius:2px;background:var(--blue-dark)}
.wait{left:834px}
.rem{left:911px;color:var(--green)}
.pm{left:981px}
.neg{color:var(--red)}.pos{color:var(--green)}
.eye{left:1024px}
.thead .wait{left:834px}.thead .rem{left:911px}.thead .pm{left:973px}
.popup{position:absolute;left:748px;top:217px;width:318px;height:206px;background:var(--white);border-radius:10px;box-shadow:0 4px 18px rgba(40,60,100,.12);z-index:5}
.popup .caret{position:absolute;left:273px;top:-7px;width:14px;height:14px;background:var(--white);transform:rotate(45deg)}
.popup h2{position:absolute;left:18px;top:15px;font-size:15.5px;font-weight:400;color:var(--blue)}
.popup .cycle{position:absolute;left:189px;top:19px;font-size:9px}
.popup .swap{position:absolute;left:157px;top:16px}
.prow{position:absolute;left:18px;width:282px;height:30px;font-size:8.3px}
.prow .ic{position:absolute;left:0;top:50%;transform:translateY(-50%)}
.prow .lbl{position:absolute;left:29px;top:50%;transform:translateY(-50%)}
.prow .pl{position:absolute;left:141px;top:50%;transform:translateY(-50%)}
.prow .ac{position:absolute;right:0;top:50%;transform:translateY(-50%)}
.psep{position:absolute;left:18px;width:282px;height:1px;background:#dcdfe6}
.overview{position:absolute;left:1098px;top:0}
.overview .h{position:absolute;top:66px;font-size:10.5px;white-space:nowrap}
.overview .k{position:absolute;font-size:8.2px;white-space:nowrap}
.overview .v{position:absolute;font-size:14px;white-space:nowrap}
.overview sup{font-size:4.5px;color:var(--red);margin-left:4px;vertical-align:8px}
.pager{position:absolute;left:1112px;top:493px;font-size:5.5px;color:#444;letter-spacing:.2px}
.scroll{position:absolute;left:1196px;top:36px;width:2px;height:280px;background:var(--blue);border-radius:1px}
</style>
</head>
<body>
<svg width="0" height="0" style="position:absolute">
  <defs>
    <symbol id="plant" viewBox="0 0 20 14"><path d="M1 14V2h3v6l4-3v3l4-3v3l4-3v9z" fill="#5a9bf0"/><rect x="4" y="10" width="2" height="1.6" fill="#fff"/><rect x="9" y="10" width="2" height="1.6" fill="#fff"/><rect x="14" y="10" width="2" height="1.6" fill="#fff"/></symbol>
    <symbol id="truck" viewBox="0 0 22 14"><rect x="0" y="1" width="14" height="9" rx="1" fill="#5a9bf0"/><path d="M14 4h4l3 3v3h-7z" fill="#5a9bf0"/><circle cx="4" cy="11.5" r="2" fill="#5a9bf0" stroke="#fff"/><circle cx="17" cy="11.5" r="2" fill="#5a9bf0" stroke="#fff"/></symbol>
    <symbol id="pin" viewBox="0 0 12 16"><path d="M6 0a6 6 0 0 1 6 6c0 4-6 10-6 10S0 10 0 6a6 6 0 0 1 6-6z" fill="#5a9bf0"/><circle cx="6" cy="6" r="2.2" fill="#fff"/></symbol>
    <symbol id="equip" viewBox="0 0 22 14"><rect x="0" y="5" width="11" height="6" fill="#5a9bf0"/><rect x="12" y="2" width="9" height="9" fill="#5a9bf0"/><rect x="14" y="4" width="2" height="2" fill="#fff"/><rect x="17" y="4" width="2" height="2" fill="#fff"/><circle cx="3" cy="12" r="2" fill="#5a9bf0" stroke="#fff"/><circle cx="8" cy="12" r="2" fill="#5a9bf0" stroke="#fff"/></symbol>
    <symbol id="eye" viewBox="0 0 16 10"><path d="M1 5s3-4 7-4 7 4 7 4-3 4-7 4-7-4-7-4z" fill="none" stroke="currentColor" stroke-width="1.4"/><circle cx="8" cy="5" r="2" fill="currentColor"/></symbol>
    <symbol id="waits" viewBox="0 0 52 12">
      <use href="#plant" x="0" y="1" width="11" height="9"/>
      <path d="M12.5 9l1.5-2.5 1.5 2.5z" fill="#e02424"/>
      <use href="#truck" x="17" y="1" width="11" height="8"/>
      <path d="M29.5 9l1.5-2.5 1.5 2.5z" fill="#e02424"/>
      <use href="#pin" x="34" y="0" width="7" height="10"/>
      <path d="M42.5 7l1.5 2.5 1.5-2.5z" fill="#22b53a"/>
    </symbol>
  </defs>
</svg>

<header class="topbar">
  <div class="menu"><span></span><span></span><span></span></div>
  <svg class="top-icon" style="left:960px" width="9" height="9" viewBox="0 0 10 10"><circle cx="4.3" cy="4.3" r="3.3" fill="none" stroke="#999" stroke-width="1"/><path d="M6.8 6.8L9.3 9.3" stroke="#999"/></svg>
  <svg class="top-icon" style="left:986px;top:15px" width="8" height="10" viewBox="0 0 8 10"><path d="M1 7V4a3 3 0 0 1 6 0v3l1 1H0z" fill="none" stroke="#999" stroke-width=".9"/><path d="M3 9h2" stroke="#999"/></svg>
  <span class="bell-dot"></span>
  <div class="user"><div class="name">Dana Mercer</div><div class="role">Manager</div></div>
  <div class="avatar" role="img" aria-label="User profile photo"></div>
</header>

<nav class="sidebar">
  <span class="active"></span>
  <svg style="top:42px" width="9" height="9" viewBox="0 0 10 10"><path d="M1 5L5 1l4 4v4H1z" fill="none" stroke="#fff"/></svg>
  <svg style="top:78px" width="9" height="9" viewBox="0 0 10 10"><path d="M5 .8l1.3 2.7 3 .4-2.2 2 .6 3L5 7.5 2.3 8.9l.6-3L.7 3.9l3-.4z" fill="none" stroke="#fff" stroke-width=".9"/></svg>
  <svg style="top:112px" width="9" height="9" viewBox="0 0 10 10"><rect x="1" y="2" width="7" height="7" fill="none" stroke="#fff"/><circle cx="8.5" cy="1.5" r="1.3" fill="#fff"/></svg>
  <svg style="top:150px" width="9" height="9" viewBox="0 0 10 10"><path d="M1 2h3l1 1h4v6H1z" fill="none" stroke="#fff"/></svg>
  <svg style="top:190px" width="10" height="10" viewBox="0 0 10 10"><circle cx="5" cy="3.2" r="2.3" fill="none" stroke="#fff"/><path d="M1 9.5a4 3.5 0 0 1 8 0z" fill="none" stroke="#fff"/></svg>
</nav>

<h1 class="page-title">Order : 17746</h1>
<div class="search">Search order number...</div>
<div class="search-btn"><svg width="10" height="10" viewBox="0 0 10 10"><circle cx="4.3" cy="4.3" r="3.3" fill="none" stroke="#fff" stroke-width="1.3"/><path d="M6.8 6.8L9.3 9.3" stroke="#fff" stroke-width="1.3"/></svg></div>
<div class="select" style="left:450px;width:188px">All</div>
<div class="select" style="left:651px;width:189px">To Date</div>
<div class="select" style="left:854px;width:189px;padding-left:20px">From Date</div>

<div class="section">Active Now</div>

<div class="thead">
  <span class="c" style="left:58px">#</span>
  <span class="c id">Order id</span>
  <span class="c org">Orgin</span>
  <span class="c dst">Destination</span>
  <span class="c cus">Customer</span>
  <span class="c sts">Status</span>
  <span class="c" style="left:689px">Tons</span>
  <span class="c wait">Wait Times</span>
  <span class="c rem">Remaining</span>
  <span class="c pm">+/- <svg width="10" height="7" viewBox="0 0 22 14"><use href="#truck"/></svg></span>
</div>
<div style="position:absolute;left:58px;top:143px;width:952px;height:1px;background:var(--line)"></div>

<div class="row" style="top:143px">
  <span class="c chk"></span><span class="c id">88038</span><span class="c org">Ridgeway Asphalt Plant</span><span class="c dst">Cedar Hill Site - Phase 7 - 8</span><span class="c cus">Halvorsen Building - North Division</span><span class="c sts">Accepted</span>
  <span class="c tons"><span class="a">722.57 / 1500</span><span class="b">7:30AM - 5:00PM</span><span class="track"><span class="fill" style="width:67px"></span></span></span>
  <svg class="c wait" width="52" height="12"><use href="#waits"/></svg>
  <span class="c rem">+1:25 hrs</span><span class="c pm neg">-31</span>
  <svg class="c eye" width="8" height="6" style="color:#555"><use href="#eye"/></svg>
</div>
<div class="row" style="top:180px">
  <span class="c chk"></span><span class="c id">88038</span><span class="c org">Ridgeway Asphalt Plant</span><span class="c dst">Cedar Hill Site - Phase 7 - 8</span><span class="c cus">Halvorsen Building - North Division</span><span class="c sts">Accepted</span>
  <span class="c tons"><span class="a">5722.57 / 500</span><span class="b">7:30AM - 5:00PM</span><span class="track"><span class="fill" style="width:45px"></span></span></span>
  <svg class="c wait" width="52" height="12"><use href="#waits"/></svg>
  <span class="c rem">+1:25 hrs</span><span class="c pm pos">+34</span>
  <svg class="c eye" width="8" height="6" style="color:var(--blue)"><use href="#eye"/></svg>
</div>
<div class="row" style="top:217px">
  <span class="c chk"></span><span class="c id">88038</span><span class="c org">Ridgeway Asphalt Plant</span><span class="c dst">Cedar Hill Site - Phase 7 - 8</span><span class="c cus">Halvorsen Building - North Division</span><span class="c sts">Accepted</span>
  <span class="c tons"><span class="a">722.57 / 1500</span><span class="b">7:30AM - 5:00PM</span><span class="track"><span class="fill" style="width:67px"></span></span></span>
</div>
<div class="row" style="top:254px">
  <span class="c chk"></span><span class="c id">88038</span><span class="c org">Ridgeway Asphalt Plant</span><span class="c dst">Cedar Hill Site - Phase 7 - 8</span><span class="c cus">Halvorsen Building - North Division</span><span class="c sts">Accepted</span>
  <span class="c tons"><span class="a">5722.57 / 500</span><span class="b">7:30AM - 5:00PM</span><span class="track"><span class="fill" style="width:45px"></span></span></span>
</div>
<div class="row" style="top:291px">
  <span class="c chk"></span><span class="c id">88038</span><span class="c org">Ridgeway Asphalt Plant</span><span class="c dst">Cedar Hill Site - Phase 7 - 8</span><span class="c cus">Halvorsen Building - North Division</span><span class="c sts">Accepted</span>
  <span class="c tons"><span class="a">722.57 / 1500</span><span class="b">7:30AM - 5:00PM</span><span class="track"><span class="fill" style="width:67px"></span></span></span>
</div>
<div class="row" style="top:328px">
  <span class="c chk"></span><span class="c id">88038</span><span class="c org">Ridgeway Asphalt Plant</span><span class="c dst">Cedar Hill Site - Phase 7 - 8</span><span class="c cus">Halvorsen Building - North Division</span><span class="c sts">Accepted</span>
  <span class="c tons"><span class="a">5722.57 / 500</span><span class="b">7:30AM - 5:00PM</span><span class="track"><span class="fill" style="width:45px"></span></span></span>
</div>
<div class="row" style="top:366px">
  <span class="c chk"></span><span class="c id">88038</span><span class="c org">Ridgeway Asphalt Plant</span><span class="c dst">Cedar Hill Site - Phase 7 - 8</span><span class="c cus">Halvorsen Building - North Division</span><span class="c sts">Accepted</span>
  <span class="c tons"><span class="a">722.57 / 1500</span><span class="b">7:30AM - 5:00PM</span><span class="track"><span class="fill" style="width:67px"></span></span></span>
</div>
<div class="row" style="top:402px">
  <span class="c chk"></span><span class="c id">88038</span><span class="c org">Ridgeway Asphalt Plant</span><span class="c dst">Cedar Hill Site - Phase 7 - 8</span><span class="c cus">Halvorsen Building - North Division</span><span class="c sts">Accepted</span>
  <span class="c tons"><span class="a">5722.57 / 500</span><span class="b">7:30AM - 5:00PM</span><span class="track"><span class="fill" style="width:45px"></span></span></span>
  <svg class="c wait" width="52" height="12"><use href="#waits"/></svg>
</div>
<div class="row" style="top:442px">
  <span class="c chk"></span><span class="c id">88038</span><span class="c org">Ridgeway Asphalt Plant</span><span class="c dst">Cedar Hill Site - Phase 7 - 8</span><span class="c cus">Halvorsen Building - North Division</span><span class="c sts">Accepted</span>
  <span class="c tons"><span class="a">722.57 / 1500</span><span class="b">7:30AM - 5:00PM</span><span class="track"><span class="fill" style="width:67px"></span></span></span>
  <svg class="c wait" width="52" height="12"><use href="#waits"/></svg>
  <span class="c rem">+1:25 hrs</span><span class="c pm neg">-31</span>
  <svg class="c eye" width="8" height="6" style="color:#555"><use href="#eye"/></svg>
</div>
<div class="row" style="top:479px">
  <span class="c chk"></span><span class="c id">88038</span><span class="c org">Ridgeway Asphalt Plant</span><span class="c dst">Cedar Hill Site - Phase 7 - 8</span><span class="c cus">Halvorsen Building - North Division</span><span class="c sts">Accepted</span>
  <span class="c tons"><span class="a">5722.57 / 500</span><span class="b">7:30AM - 5:00PM</span><span class="track"><span class="fill" style="width:45px"></span></span></span>
  <svg class="c wait" width="52" height="12"><use href="#waits"/></svg>
  <span class="c rem">+1:25 hrs</span><span class="c pm pos">+34</span>
  <svg class="c eye" width="8" height="6" style="color:#555"><use href="#eye"/></svg>
</div>

<section class="popup">
  <span class="caret"></span>
  <h2>Order : 17746</h2>
  <svg class="swap" width="16" height="12" viewBox="0 0 16 12"><path d="M1 4h13l-3-3M15 8H2l3 3" fill="none" stroke="#5a9bf0" stroke-width="1.3"/></svg>
  <div class="cycle">Avg Cycle Time: 2hr 27min</div>
  <div class="psep" style="top:49px"></div>
  <div class="prow" style="top:53px"><svg class="ic" width="21" height="17"><use href="#plant"/></svg><span class="lbl">Plant (min)</span><span class="pl">Planed: 30</span><span class="ac">Actual: 33</span></div>
  <div class="psep" style="top:84px"></div>
  <div class="prow" style="top:89px"><svg class="ic" width="21" height="14"><use href="#truck"/></svg><span class="lbl">Driving (min)</span><span class="pl">Planed: 60</span><span class="ac">Actual: 83</span></div>
  <div class="psep" style="top:123px"></div>
  <div class="prow" style="top:128px"><svg class="ic" width="21" height="17"><use href="#pin" x="5" width="11" height="17"/></svg><span class="lbl">Jobsite (min)</span><span class="pl">Planed: 30</span><span class="ac">Actual: 30</span></div>
  <div class="psep" style="top:162px"></div>
  <div class="prow" style="top:166px"><svg class="ic" width="22" height="13"><use href="#equip"/></svg><span class="lbl">Equipment (min)</span><span class="ac" style="right:14px">Actual</span></div>
</section>

<aside class="overview">
  <div class="h">OVERVIEW</div>
  <div class="k" style="top:104px">Orders Today</div><div class="v" style="top:119px">235</div>
  <div class="k" style="top:154px">Pending Orders</div><div class="v" style="top:169px">23</div>
  <div class="k" style="top:208px">Delivered</div><div class="v" style="top:224px">125<sup>-3%</sup></div>
  <div class="k" style="top:250px">Cancelled</div><div class="v" style="top:265px">25</div>
</aside>
<div class="pager">1-3 OF 3 &nbsp;‹ ›</div>
<div class="scroll"></div>
</body>
</html>
```